Notevo App
Notevo App - Utilities
Creative Brief
I need two designs for the app, included are the draft designs of what I need, I have uploaded them, I have also included the app icon, in red, I need two pages, one with the pictures and send buttons, and one for the read messages page, bear in mind that the pictures page can hold from 1 to 9 pictures max.
Utilities
utilities app for iOS and android

```html
<!DOCTYPE html>
<html lang="en">
<head>
<meta charset="utf-8">
<title>Notevo App – Screens</title>
<link href="https://fonts.googleapis.com/css2?family=Roboto:wght@400;700;900&display=swap" rel="stylesheet">
<style>
:root{
  --bg:#e9e9e9;
  --red:#e3191f;
  --red-dark:#b80f14;
  --ink:#111;
  --grey:#9a9a9a;
  --light:#f2f2f2;
  --white:#fff;
  --photo:#8a7f78;
}
*{box-sizing:border-box;margin:0;padding:0}
html,body{width:1200px;height:602px;overflow:hidden}
body{background:var(--bg);font-family:"Roboto",Arial,sans-serif;color:var(--ink);position:relative}
.brand{position:absolute;font-weight:900;letter-spacing:-1px;color:var(--ink)}
.hero-name{left:34px;top:70px;font-size:44px}
.icon-set{position:absolute;left:34px;top:170px}
.icon-large{width:150px;height:150px;border-radius:30px;background:var(--red);border:5px solid #ccc;display:flex;align-items:center;justify-content:center;color:var(--white);font-weight:900;font-size:30px}
.icon-small{position:absolute;background:var(--red);border-radius:6px;border:2px solid #ccc}
.icon-caption{position:absolute;left:40px;top:164px;font-size:9px;color:#666;width:80px;text-align:center}
.screen{position:absolute;top:80px;width:190px;height:440px;background:var(--white);overflow:hidden;box-shadow:0 2px 10px rgba(0,0,0,.25)}
.status{height:14px;background:#000;color:var(--white);font-size:8px;display:flex;justify-content:space-between;align-items:center;padding:0 5px}
.loading-screen{left:370px}
.loading-screen .brand{position:absolute;left:0;right:0;top:190px;text-align:center;font-size:28px}
.loading-text{position:absolute;left:0;right:0;top:300px;text-align:center;font-size:8px;color:var(--red)}
.pictures-screen{left:620px}
.header{height:36px;display:flex;align-items:center;justify-content:center;font-weight:900;font-size:22px;letter-spacing:-1px}
.tools{display:flex;justify-content:center;gap:16px;padding:4px 0 8px}
.tool{width:28px;height:26px;border-radius:5px;background:linear-gradient(#fafafa,#d5d5d5);border:1px solid #bbb;display:flex;align-items:center;justify-content:center}
.grid{display:grid;grid-template-columns:repeat(3,52px);gap:8px 6px;justify-content:center}
.tile{border:2px solid var(--red);background:var(--red)}
.photo{display:block;height:52px;background:linear-gradient(160deg,#b2a69c,var(--photo))}
.tile-label{font-size:6px;color:var(--white);text-align:center;height:9px;line-height:9px}
.send{position:absolute;right:12px;bottom:30px;background:var(--red);color:var(--white);font-size:8px;font-weight:700;padding:4px 12px;border-radius:10px}
.messages-screen{left:930px}
.header-red{height:30px;background:var(--white);border-bottom:3px solid var(--red);display:flex;align-items:center;justify-content:space-between;padding:0 6px;font-weight:900;font-size:19px;letter-spacing:-1px}
.hbtn{width:16px;height:14px;background:var(--red);border-radius:3px}
.row{display:flex;align-items:center;margin:6px 6px 0;height:46px;border:2px solid var(--red);border-radius:3px;padding:3px;position:relative}
.row .photo{width:36px;height:36px}
.info{margin-left:6px;font-size:6px;line-height:9px;color:#555}
.info b{color:var(--red)}
.tag{position:absolute;right:-2px;top:13px;background:#000;color:var(--white);font-size:6px;padding:2px 6px 2px 10px;clip-path:polygon(8px 0,100% 0,100% 100%,8px 100%,0 50%)}
</style>
</head>
<body>
<div class="brand hero-name">Notevo</div>
<div class="icon-set">
  <div class="icon-large">Notevo</div>
  <div class="icon-small" style="left:172px;top:10px;width:34px;height:34px"></div>
  <div class="icon-small" style="left:176px;top:56px;width:26px;height:26px"></div>
  <div class="icon-small" style="left:179px;top:92px;width:20px;height:20px"></div>
  <div class="icon-small" style="left:181px;top:120px;width:16px;height:16px"></div>
  <div class="icon-caption">App Icon 512x512</div>
</div>

<section class="screen loading-screen">
  <div class="status"><span>Telvo</span><span>12:00 PM</span><span>▮▮</span></div>
  <div class="brand">Notevo</div>
  <div class="loading-text">Loading...</div>
</section>

<section class="screen pictures-screen">
  <div class="status"><span>Telvo</span><span>12:00 PM</span><span>▮▮</span></div>
  <div class="header">Notevo</div>
  <div class="tools">
    <div class="tool"><svg width="12" height="14" viewBox="0 0 12 14"><rect x="4" y="1" width="4" height="8" rx="2" fill="#333"/><path d="M2 7a4 4 0 0 0 8 0M6 11v2" stroke="#333" fill="none"/></svg></div>
    <div class="tool"><svg width="14" height="12" viewBox="0 0 14 12"><path d="M1 1h12v7H5l-3 3V8H1z" fill="#333"/></svg></div>
    <div class="tool"><svg width="14" height="12" viewBox="0 0 14 12"><rect x="1" y="3" width="12" height="8" rx="1" fill="#333"/><rect x="4" y="1" width="6" height="3" fill="#333"/><circle cx="7" cy="7" r="2.3" fill="#ddd"/></svg></div>
  </div>
  <div class="grid">
    <div class="tile"><span class="photo" role="img" aria-label="Contact photo"></span><div class="tile-label">Likes 12</div></div>
    <div class="tile"><span class="photo" role="img" aria-label="Contact photo"></span><div class="tile-label">Likes 12</div></div>
    <div class="tile"><span class="photo" role="img" aria-label="Contact photo"></span><div class="tile-label">Likes 12</div></div>
    <div class="tile"><span class="photo" role="img" aria-label="Contact photo"></span><div class="tile-label">Likes 12</div></div>
    <div class="tile"><span class="photo" role="img" aria-label="Contact photo"></span><div class="tile-label">Likes 12</div></div>
    <div class="tile"><span class="photo" role="img" aria-label="Contact photo"></span><div class="tile-label">Likes 12</div></div>
    <div class="tile"><span class="photo" role="img" aria-label="Contact photo"></span><div class="tile-label">Likes 12</div></div>
    <div class="tile"><span class="photo" role="img" aria-label="Contact photo"></span><div class="tile-label">Likes 12</div></div>
    <div class="tile"><span class="photo" role="img" aria-label="Contact photo"></span><div class="tile-label">Likes 12</div></div>
  </div>
  <div class="send">SEND</div>
</section>

<section class="screen messages-screen">
  <div class="status"><span>Telvo</span><span>12:00 PM</span><span>▮▮</span></div>
  <div class="header-red"><span class="hbtn"></span>Notevo<span class="hbtn"></span></div>
  <div class="row"><span class="photo" role="img" aria-label="Sender photo"></span><div class="info"><b>Ana Reyes</b><br>N/A<br>12 km</div><span class="tag">Likes 12</span></div>
  <div class="row"><span class="photo" role="img" aria-label="Sender photo"></span><div class="info"><b>Tom Hale</b><br>N/A<br>12 km</div><span class="tag">Likes 12</span></div>
  <div class="row"><span class="photo" role="img" aria-label="Sender photo"></span><div class="info"><b>Lia Moss</b><br>N/A<br>12 km</div><span class="tag">Likes 12</span></div>
  <div class="row"><span class="photo" role="img" aria-label="Sender photo"></span><div class="info"><b>Ben Cole</b><br>N/A<br>12 km</div><span class="tag">Likes 12</span></div>
  <div class="row"><span class="photo" role="img" aria-label="Sender photo"></span><div class="info"><b>Eva Park</b><br>N/A<br>12 km</div><span class="tag">Likes 12</span></div>
  <div class="row"><span class="photo" role="img" aria-label="Sender photo"></span><div class="info"><b>Max Dorn</b><br>N/A<br>12 km</div><span class="tag">Likes 12</span></div>
  <div class="row"><span class="photo" role="img" aria-label="Sender photo"></span><div class="info"><b>Ida Lund</b><br>N/A<br>12 km</div><span class="tag">Likes 12</span></div>
</section>
</body>
</html>
```